New Dental Office Needs an Attractive and user friendly Website Designed

I need a website for a new dental office. The Name is Maplecrest Dentistry. I would like a Modern design with a user friendly interface and usability.
I would like a landing page, a page that lists the services we offer: Cosmetic Dentistry, Implants, Dental Hygiene, Emergency Services, Restorations, Dentures
Target Market(s)
Mid to upper class
Industry/Entity Type
Dentistry
Coding
Coded - Design and coding required
Number of Pages Required
1 page
Requirements
Must have
- Landing page that has a scheduling option, Procedures, operating hours, and contact us info
Nice to have
- Appealing design, Soft comforting colors. Easy to navigate page, Modern and professional.

```html
<!DOCTYPE html>
<html lang="en">
<head>
<meta charset="utf-8">
<title>Maplecrest Dentistry</title>
<link href="https://fonts.googleapis.com/css2?family=Urbanist:wght@400;500;600;700;800&family=Kalam:wght@700&display=swap" rel="stylesheet">
<style>
:root{
  --blue:#2fa3f5;
  --blue-deep:#1a8fe8;
  --sky:#e2f2fd;
  --sky-soft:#eef8ff;
  --ink:#111418;
  --muted:#6b7480;
  --white:#ffffff;
  --field:#eef0f3;
  --dark:#2b2b2b;
  --line:#d9e3ea;
}
*{box-sizing:border-box;margin:0;padding:0}
html,body{width:1200px;height:3759px;overflow:hidden}
body{font-family:"Urbanist",sans-serif;color:var(--ink);background:var(--white);position:relative}
.abs{position:absolute}
.brand{font-family:"Urbanist",sans-serif;font-weight:700;color:var(--ink);font-size:21px;letter-spacing:.2px}
/* nav */
.nav{top:0;left:0;width:1200px;height:62px}
.nav .brand{left:66px;top:20px}
.nav-links{left:584px;top:26px;display:flex;gap:31px;font-size:12.5px;font-weight:500}
.btn{display:flex;align-items:center;justify-content:center;border-radius:30px;font-weight:600;font-size:11.5px}
.btn-blue{background:var(--blue);color:var(--white);box-shadow:0 6px 14px rgba(47,163,245,.35)}
.btn-white{background:var(--white);color:var(--blue)}
.nav .btn{left:1048px;top:16px;width:89px;height:36px}
/* hero */
.hero-main{left:62px;top:62px;width:1075px;height:408px;background:var(--blue);border-radius:30px 30px 30px 0}
.hero-tail{left:62px;top:440px;width:188px;height:235px;background:var(--blue);border-radius:0 0 0 30px}
.hero-title{left:188px;top:138px;font-family:"Kalam",cursive;font-weight:700;font-size:60px;line-height:64px;color:var(--white)}
.hero-sub{left:187px;top:285px;font-size:18px;line-height:24px;color:var(--white);font-weight:500}
.hero .btn{left:187px;top:355px;width:122px;height:36px}
.hero-art{left:520px;top:92px;width:580px;height:378px;border-radius:40px;background:radial-gradient(ellipse at 55% 50%,#ffffff 0%,#cfe9fc 30%,rgba(47,163,245,0) 65%)}
.booking-wrap{left:250px;top:470px;width:887px;height:208px;background:#f2f9ff;border-radius:30px 0 0 0}
.booking-card{left:275px;top:497px;width:837px;height:178px;background:var(--white);border-radius:16px 16px 0 0}
.booking-title{left:333px;top:546px;font-size:30px;font-weight:700;line-height:40px}
.label{font-size:14px;font-weight:600}
.select{height:30px;width:187px;background:var(--field);border-radius:15px;font-size:11.5px;color:#8a929b;display:flex;align-items:center;justify-content:space-between;padding:0 14px}
.select svg{width:9px;height:6px}
/* about */
.about{top:678px;left:0;width:1200px;height:627px;background:var(--sky)}
.pill{height:20px;padding:0 10px;border-radius:10px;background:var(--blue);color:var(--white);font-size:9px;font-weight:600;display:flex;align-items:center;gap:5px;box-shadow:0 0 0 2px #fff,0 3px 8px rgba(0,0,0,.15)}
.about-head{left:198px;top:774px;font-size:22px;font-weight:600;line-height:28px;letter-spacing:-.3px;white-space:nowrap}
.card{background:var(--white);border-radius:8px}
.tag{font-size:8px;color:var(--blue);border:1px solid #cde6fa;border-radius:10px;padding:3px 8px;display:inline-block}
.arrow-sq{width:24px;height:24px;background:var(--blue);border-radius:5px;display:flex;align-items:center;justify-content:center}
.small-copy{font-size:11.5px;line-height:17.5px;color:#2b2f35}
.photo{border-radius:10px}
.bluecard{left:820px;top:876px;width:186px;height:367px;background:var(--blue);border-radius:8px;color:var(--white)}
.chip{font-size:9px;border:1px solid rgba(255,255,255,.5);background:rgba(255,255,255,.12);border-radius:10px;padding:4px 9px;display:inline-block;margin-bottom:9px}
/* why */
.why-bg{top:1305px;left:0;width:1200px;height:470px;background:radial-gradient(ellipse at 12% 70%,#e6f2fb 0%,rgba(255,255,255,0) 40%),radial-gradient(ellipse at 90% 12%,#e3f1fc 0%,rgba(255,255,255,0) 35%)}
.why-title{left:602px;top:1440px;font-size:31px;font-weight:700;line-height:41px}
.why-text{left:602px;top:1532px;font-size:14px;line-height:20px;color:var(--muted);width:400px}
.check{display:flex;align-items:center;gap:10px;font-size:15px;font-weight:500}
.tick{width:18px;height:18px;border-radius:50%;background:var(--blue);display:flex;align-items:center;justify-content:center}
/* services */
.center{left:0;width:1200px;text-align:center}
.sec-title{font-size:31px;font-weight:700}
.sec-sub{font-size:14px;color:var(--muted)}
.svc-box{background:#e8f5fd;border-radius:8px}
.svc-name{font-size:22px;font-weight:600;line-height:34px}
.go{width:24px;height:24px;border-radius:50%;background:var(--ink);display:flex;align-items:center;justify-content:center}
/* testimonials */
.testi{top:2506px;left:0;width:1200px;height:500px;background:var(--sky)}
.quote{left:360px;top:2775px;width:480px;font-size:19.5px;line-height:27px;text-align:center}
.circle-arrow{width:30px;height:30px}
/* consultation */
.consult{left:227px;top:3078px;width:743px;height:317px;background:var(--white);border-radius:8px;box-shadow:0 10px 30px rgba(30,90,140,.12);overflow:hidden}
.field{width:173px;height:45px;border:1.5px solid var(--line);border-radius:10px;font-size:11.5px;color:#8a929b;display:flex;align-items:center;padding-left:32px}
/* footer */
.footer{top:3468px;left:0;width:1200px;height:291px;background:var(--dark);color:var(--white)}
.f-head{font-size:12px;font-weight:600}
.f-list{font-size:10.5px;line-height:20px;color:#d7d7d7}
.social{display:flex;gap:9px}
.social span{width:17px;height:17px;border-radius:50%;background:var(--white)}
</style>
</head>
<body>

<header class="abs nav">
  <div class="abs brand">Maplecrest Dentistry</div>
  <nav class="abs nav-links"><span>Home</span><span>About Us</span><span>Services</span><span>Schedule Appointment</span><span>Contact</span></nav>
  <a class="abs btn btn-blue">Book now</a>
</header>

<section class="hero">
  <div class="abs hero-main"></div>
  <div class="abs hero-tail"></div>
  <div class="abs hero-art" role="img" aria-label="Glossy white tooth wrapped in light swirls with flying green leaves"></div>
  <h1 class="abs hero-title">Your Smile,<br>Our Priority</h1>
  <p class="abs hero-sub">Personalized, gentle dental<br>care in a calm and modern setting.</p>
  <a class="abs btn btn-white">Explore Services</a>

  <div class="abs booking-wrap"></div>
  <div class="abs booking-card"></div>
  <h2 class="abs booking-title">Book an<br>Appointment</h2>
  <div class="abs label" style="left:600px;top:518px">Appointment Date</div>
  <div class="abs select" style="left:600px;top:548px">Select date<svg viewBox="0 0 9 6"><path d="M0 0h9L4.5 6z" fill="#555"/></svg></div>
  <div class="abs label" style="left:825px;top:518px">Persons</div>
  <div class="abs select" style="left:825px;top:548px">2 adults<svg viewBox="0 0 9 6"><path d="M0 0h9L4.5 6z" fill="#555"/></svg></div>
  <div class="abs label" style="left:600px;top:590px">Location</div>
  <div class="abs select" style="left:600px;top:619px">Select your location<svg viewBox="0 0 9 6"><path d="M0 0h9L4.5 6z" fill="#555"/></svg></div>
  <a class="abs btn btn-blue" style="left:825px;top:619px;width:89px;height:35px">Book now</a>
</section>

<section class="abs about"></section>
<div class="abs pill" style="left:198px;top:744px">• About •</div>
<h2 class="abs about-head">Compassionate Care. Advanced<br>Dentistry. Trusted Smiles. <svg width="38" height="14" viewBox="0 0 38 14" style="vertical-align:middle"><path d="M2 3 Q19 18 36 3 Q19 10 2 3z" fill="#2fa3f5"/></svg> exceptional<br>care in a warm, welcoming environment.</h2>

<div class="abs card" style="left:198px;top:876px;width:340px;height:184px"></div>
<span class="abs tag" style="left:215px;top:896px">WHO WE ARE</span>
<div class="abs arrow-sq" style="left:499px;top:890px"><svg width="12" height="12" viewBox="0 0 12 12"><path d="M2 6h8M6 2l4 4-4 4" stroke="#fff" stroke-width="1.6" fill="none"/></svg></div>
<p class="abs small-copy" style="left:215px;top:960px;width:310px">At Maplecrest Dentistry, we believe your dental experience should be as comfortable as it is effective. We're a team of experienced professionals committed to providing personalized care in a calm, welcoming environment.</p>

<div class="abs photo" style="left:550px;top:876px;width:258px;height:184px;background:linear-gradient(135deg,#cfe3ef,#3a9fb6 55%,#e9eef2)" role="img" aria-label="Dentist in teal scrubs examining a smiling patient in the chair"></div>

<div class="abs bluecard">
  <div class="abs brand" style="left:17px;top:16px;color:#fff;font-size:16px">Maplecrest Dentistry</div>
  <p class="abs" style="left:17px;top:58px;width:156px;font-size:9.5px;line-height:13px">Our team at Maplecrest Clinic is here to provide you with expert dental care in a comfortable and welcoming environment.</p>
  <div class="abs" style="left:17px;top:212px;width:160px">
    <span class="chip">Comprehensive Services</span><br><span class="chip">Experienced Professionals</span><br><span class="chip">State-of-the-Art Technology</span><br><span class="chip">Personalized Treatment Plans</span><br><span class="chip">Relaxing Environment</span>
  </div>
</div>

<div class="abs" style="left:198px;top:1073px;width:193px;height:170px;background:#bfe6fb;border-radius:8px"></div>
<svg class="abs" style="left:268px;top:1108px" width="52" height="40" viewBox="0 0 52 40"><path d="M6 4c8-6 16 2 20 2s12-8 20-2c6 5 2 16-3 22-3 4-5 12-9 12-3 0-3-8-8-8s-5 8-8 8c-4 0-6-8-9-12C4 20 0 9 6 4z" fill="#6cc3f7"/></svg>
<p class="abs" style="left:198px;top:1168px;width:193px;text-align:center;font-size:16px;line-height:20px;color:var(--blue);font-weight:500">Your health is<br>our priority.</p>

<div class="abs card" style="left:403px;top:1073px;width:405px;height:170px"></div>
<span class="abs tag" style="left:420px;top:1092px">EXCLUSIVE DISCOUNTS</span>
<div class="abs arrow-sq" style="left:769px;top:1088px"><svg width="12" height="12" viewBox="0 0 12 12"><path d="M2 6h8M6 2l4 4-4 4" stroke="#fff" stroke-width="1.6" fill="none"/></svg></div>
<p class="abs small-copy" style="left:420px;top:1150px;width:335px">At Maplecrest Clinic, we believe everyone deserves access to high-quality dental care. To make it easier for you to maintain your oral health, we offer exclusive discounts on a variety of services.</p>

<section class="abs why-bg"></section>
<div class="abs photo" style="left:207px;top:1380px;width:273px;height:325px;background:linear-gradient(160deg,#eef1f3,#dcdfe2 60%,#bfc4c8)" role="img" aria-label="Smiling female dentist in white coat holding dental tools"></div>
<div class="abs photo" style="left:383px;top:1553px;width:157px;height:165px;border:3px solid #fff;background:linear-gradient(150deg,#f0c7c9,#8fd0ea 60%,#3c9fd2)" role="img" aria-label="Patient smiling during a dental check-up"></div>
<div class="abs pill" style="left:602px;top:1409px">• Who we are •</div>
<h2 class="abs why-title">Why Our Dental Care is<br>Preferred</h2>
<p class="abs why-text">Your comfort, your health, and your smile are at the heart of everything we do.</p>
<div class="abs check" style="left:602px;top:1587px"><span class="tick"><svg width="10" height="8" viewBox="0 0 10 8"><path d="M1 4l3 3 5-6" stroke="#fff" stroke-width="1.6" fill="none"/></svg></span>Expert Advice Ide Planner</div>
<div class="abs check" style="left:602px;top:1617px"><span class="tick"><svg width="10" height="8" viewBox="0 0 10 8"><path d="M1 4l3 3 5-6" stroke="#fff" stroke-width="1.6" fill="none"/></svg></span>Make Your Smile Beautiful</div>
<a class="abs btn btn-blue" style="left:602px;top:1656px;width:93px;height:34px">Read More</a>

<div class="abs pill" style="left:559px;top:1796px">• Our Services •</div>
<h2 class="abs center sec-title" style="top:1825px">Comprehensive Dental Services</h2>
<p class="abs center sec-sub" style="top:1873px">From routine check-ups to advanced cosmetic procedures</p>

<div class="abs svc-box" style="left:190px;top:1911px;width:417px;height:195px"></div>
<h3 class="abs" style="left:207px;top:1922px;font-size:29px;font-weight:700">Smile Gallery</h3>
<p class="abs" style="left:207px;top:2077px;font-size:12px;font-weight:500">Our Cosmetic dental works</p>
<div class="abs svc-box" style="left:190px;top:2117px;width:417px;height:133px"></div>
<h3 class="abs" style="left:208px;top:2125px;font-size:51px;font-weight:700;line-height:56px">Smile<br>makeover</h3>
<div class="abs" style="left:613px;top:1911px;width:402px;height:339px;border-radius:8px;background:linear-gradient(180deg,#d9eef9 0%,#e6d6c9 45%,#f2c64b 80%,#f7d25c)" role="img" aria-label="Smiling woman in a yellow sweater resting her chin on her hands"></div>

<div class="abs svc-box" style="left:190px;top:2256px;width:825px;height:174px"></div>
<div class="abs card" style="left:203px;top:2265px;width:225px;height:155px"></div>
<div class="abs" style="left:333px;top:2273px;width:72px;height:44px;border-radius:8px;background:linear-gradient(180deg,#f0f0f0,#e2474f)" role="img" aria-label="Model of teeth with metal braces"></div>
<h3 class="abs svc-name" style="left:221px;top:2307px">Braces</h3>
<p class="abs" style="left:221px;top:2353px;width:195px;font-size:11px;line-height:17px">Traditional metal braces are the most common type of orthodontic treatment</p>

<div class="abs" style="left:440px;top:2265px;width:225px;height:155px;border-radius:8px;background:linear-gradient(120deg,#e8f5fd 45%,#f0d9a8 75%,#2a2420)" role="img" aria-label="Blurred photo of denture work"></div>
<h3 class="abs svc-name" style="left:460px;top:2280px">Prosthodontics<br>Dentures</h3>
<div class="abs go" style="left:628px;top:2384px"><svg width="10" height="10" viewBox="0 0 10 10"><path d="M3 2l4 3-4 3" stroke="#fff" stroke-width="1.6" fill="none"/></svg></div>

<div class="abs" style="left:678px;top:2265px;width:225px;height:155px;border-radius:8px;background:linear-gradient(120deg,#fbd867,#f0c04a 70%,#c9a570)" role="img" aria-label="Blurred photo of ceramic braces"></div>
<h3 class="abs svc-name" style="left:697px;top:2280px">Ceramic<br>Braces</h3>
<div class="abs go" style="left:866px;top:2384px"><svg width="10" height="10" viewBox="0 0 10 10"><path d="M3 2l4 3-4 3" stroke="#fff" stroke-width="1.6" fill="none"/></svg></div>

<div class="abs" style="left:915px;top:2265px;width:100px;height:155px;border-radius:8px 0 0 8px;background:linear-gradient(120deg,#f6e7c6,#f3c350)" role="img" aria-label="Blurred photo of clear aligners"></div>
<h3 class="abs svc-name" style="left:925px;top:2280px;font-size:20px">Clear<br>Aligners</h3>

<section class="abs testi"></section>
<div class="abs" style="left:225px;top:2560px;width:750px;height:400px;background:radial-gradient(ellipse at center,rgba(160,180,195,.28) 0%,rgba(226,242,253,0) 70%)" role="img" aria-label="Dotted world map with small patient portraits"></div>
<div class="abs pill" style="left:559px;top:2583px">• Testimonials •</div>
<h2 class="abs center sec-title" style="top:2618px;font-size:30px">What Our Patients Say</h2>
<div class="abs" style="left:558px;top:2664px;width:72px;height:72px;border-radius:50%;background:linear-gradient(160deg,#f3d9d2,#e4b9a9)" role="img" aria-label="Portrait of the reviewing patient"></div>
<p class="abs quote">Maplecrest Dentistry completely changed how I feel about dental visits. The team is so gentle and welcoming. I actually look forward to my appointments now</p>
<p class="abs center" style="top:2912px;font-size:14.5px;font-weight:700">Daniel Reyes</p>
<p class="abs center" style="top:2933px;font-size:12px;color:#444">Detroit, Michigan</p>
<svg class="abs circle-arrow" style="left:246px;top:2806px" viewBox="0 0 30 30"><circle cx="15" cy="15" r="13.5" fill="none" stroke="#111" stroke-width="1.4"/><path d="M21 15H9M14 10l-5 5 5 5" stroke="#111" stroke-width="1.4" fill="none"/></svg>
<svg class="abs circle-arrow" style="left:923px;top:2806px" viewBox="0 0 30 30"><circle cx="15" cy="15" r="13.5" fill="none" stroke="#111" stroke-width="1.4"/><path d="M9 15h12M16 10l5 5-5 5" stroke="#111" stroke-width="1.4" fill="none"/></svg>

<section class="consult abs">
  <div class="abs" style="left:0;top:0;width:305px;height:317px;background:linear-gradient(160deg,#e6f4fd,#cfe8fa)" role="img" aria-label="Smiling dentist in white coat and blue gloves pointing toward the form"></div>
</section>
<h2 class="abs" style="left:582px;top:3112px;width:364px;text-align:center;font-size:29px;font-weight:700">Free Consultation</h2>
<div class="abs field" style="left:582px;top:3175px">Full Name*</div>
<div class="abs field" style="left:771px;top:3175px">I'm interested in*</div>
<div class="abs field" style="left:582px;top:3240px">Email*</div>
<div class="abs field" style="left:771px;top:3240px">Phone Number*</div>
<a class="abs btn btn-blue" style="left:582px;top:3308px;width:364px;height:46px;font-size:12.5px;gap:8px">Get a Free Consultation <svg width="12" height="12" viewBox="0 0 12 12"><path d="M2 2l8 8M10 3v7H3" stroke="#fff" stroke-width="1.6" fill="none"/></svg></a>

<footer class="abs footer">
  <div class="abs brand" style="left:0;width:1200px;text-align:center;top:34px;color:#fff;font-size:19px">Maplecrest Dentistry</div>
  <div class="abs" style="left:185px;top:92px"><div class="f-head">Menu</div><div class="f-list" style="margin-top:10px"><span style="color:var(--blue)">Home</span><br>About Us<br>Services<br>Schedule Appointment<br>Contact Us</div></div>
  <div class="abs" style="left:367px;top:92px"><div class="f-head">Legal Links</div><div class="f-list" style="margin-top:10px">Privacy Policy<br>Terms &amp; Conditions</div></div>
  <div class="abs" style="left:367px;top:188px"><div class="f-head">Operating Hours</div><div class="f-list" style="margin-top:8px;line-height:15px">Mon — Fri: 9:00 AM — 6:00 PM<br>Sat: 9:00 AM — 1:00 PM<br>Sun: Closed</div></div>
  <div class="abs" style="left:599px;top:92px"><div class="f-head">Address</div><div class="f-list" style="margin-top:10px;line-height:15px">123 Maplecrest Avenue, [City],<br>[State], [ZIP]<br><u>View on Maps</u></div></div>
  <div class="abs" style="left:599px;top:190px"><div class="f-head">Inquiries</div><div class="f-list" style="margin-top:8px;line-height:15px">(123) 456-7890<br>info@maplecrestdental.com</div></div>
  <div class="abs" style="left:823px;top:92px"><div class="f-head">Newsletter</div><div class="f-list" style="margin-top:4px">Stay Updated with our Latest News</div></div>
  <div class="abs" style="left:823px;top:134px;width:191px;height:36px;border:1.5px solid #fff;border-radius:18px;font-size:12px;display:flex;align-items:center;padding-left:12px">Your Email</div>
  <div class="abs" style="left:968px;top:140px;width:40px;height:24px;border-radius:12px;background:var(--blue);display:flex;align-items:center;justify-content:center"><svg width="14" height="10" viewBox="0 0 14 10"><path d="M1 5h11M8 1l4 4-4 4" stroke="#fff" stroke-width="1.5" fill="none"/></svg></div>
  <div class="abs f-head" style="left:823px;top:218px;font-weight:500">Follow Us</div>
  <div class="abs social" style="left:823px;top:240px"><span></span><span></span><span></span><span></span><span></span><span></span><span></span></div>
</footer>

</body>
</html>
```